Business card design Needed for new logo / Construction business, home extensions and new builds

We need a business card design using our new logo files which i will attach to this project :)

We are a small construction business specialising in home extensions, new builds and property development. We are very ambitious and would appreciate professional and elegant designs for our new business card.

Very serious about using the services on BriefNest and recently acquired our new logo from here :)

Please get involved, i will feedback when i can as i am very busy but can respond daily, thanks

Target Market(s)

People that want to build onto their houses, new building developments or adding too their existing property

Industry/Entity Type

Construction

Contact Information for Business Card

Hollin Marsh Construction, Tobias Renwick (Managing Director), Tel 07822200444, email - info@hollin-marsh, www.hollin-marsh.co.uk

Colors

Designer to choose colors to be used in the design.

Requirements
Must have
• I like a deep grey on the back please. A lot of you have provided black from and back, try mixing things up a little. The black looks cool 😎 Thanks

```html
<!DOCTYPE html>
<html lang="en">
<head>
<meta charset="utf-8">
<title>Hollin Marsh Construction – Business Card</title>
<link rel="stylesheet" href="https://fonts.googleapis.com/css2?family=Cinzel:wght@600&family=Arimo:wght@400;700&display=swap">
<style>
  :root {
    --backdrop: #2a2a2c;
    --gold-light: #ecc979;
    --gold-mid: #d2a24f;
    --gold-deep: #a9702a;
    --charcoal: #2b2b2d;
    --silver-light: #d6d8dc;
    --silver-deep: #8e9096;
    --ink: #1d1d1f;
  }
  html, body {
    margin: 0;
    width: 1200px;
    height: 960px;
    overflow: hidden;
    background: var(--backdrop);
  }
  .sheet {
    position: relative;
    width: 1200px;
    height: 960px;
  }
  .card {
    position: absolute;
    left: 250px;
    width: 700px;
    height: 400px;
    border-radius: 28px;
    overflow: hidden;
    box-shadow: 0 18px 40px rgba(0,0,0,0.45);
  }
  .card--front {
    top: 50px;
    background: radial-gradient(ellipse at 50% 35%, var(--gold-light) 0%, var(--gold-mid) 55%, var(--gold-deep) 100%);
    display: flex;
    flex-direction: column;
    align-items: center;
    justify-content: center;
    gap: 18px;
  }
  .brand-mark {
    width: 22px;
    height: 22px;
    background: var(--ink);
  }
  .brand-name {
    margin: 0;
    font-family: "Cinzel", serif;
    font-weight: 600;
    font-size: 34px;
    line-height: 1.2;
    letter-spacing: 1px;
    text-align: center;
    color: var(--ink);
  }
  .card--back {
    top: 510px;
  }
  .card-bg {
    position: absolute;
    inset: 0;
    width: 100%;
    height: 100%;
  }
  .back-brand {
    position: absolute;
    left: 40px;
    top: 120px;
    width: 290px;
    margin: 0;
    font-family: "Cinzel", serif;
    font-weight: 600;
    font-size: 27px;
    line-height: 1.25;
    letter-spacing: 1px;
    text-align: center;
    color: var(--gold-mid);
  }
  .contact {
    position: absolute;
    right: 40px;
    top: 130px;
    margin: 0;
    padding: 0;
    list-style: none;
    font-family: "Arimo", sans-serif;
    font-size: 19px;
    color: var(--ink);
    text-align: right;
  }
  .contact li {
    display: flex;
    justify-content: flex-end;
    align-items: center;
    gap: 10px;
    line-height: 28px;
  }
  .contact svg {
    width: 16px;
    height: 16px;
    fill: var(--ink);
  }
  .person {
    position: absolute;
    right: 66px;
    top: 265px;
    text-align: right;
    font-family: "Arimo", sans-serif;
    color: var(--ink);
  }
  .person-name {
    margin: 0;
    font-size: 32px;
    font-weight: 700;
  }
  .person-role {
    margin: 4px 0 0;
    font-size: 21px;
  }
</style>
</head>
<body>
<main class="sheet">
  <section class="card card--front" aria-label="Card front">
    <span class="brand-mark" aria-hidden="true"></span>
    <p class="brand-name">Hollin Marsh<br>Construction</p>
  </section>

  <section class="card card--back" aria-label="Card back">
    <svg class="card-bg" viewBox="0 0 700 400" preserveAspectRatio="none" aria-hidden="true">
      <defs>
        <radialGradient id="goldPanel" cx="75%" cy="40%" r="70%">
          <stop offset="0" stop-color="#ecc979"/>
          <stop offset="0.55" stop-color="#d2a24f"/>
          <stop offset="1" stop-color="#a9702a"/>
        </radialGradient>
        <linearGradient id="silverBand" x1="0" y1="1" x2="1" y2="0">
          <stop offset="0" stop-color="#8e9096"/>
          <stop offset="0.5" stop-color="#d6d8dc"/>
          <stop offset="1" stop-color="#8e9096"/>
        </linearGradient>
      </defs>
      <rect width="700" height="400" fill="url(#goldPanel)"/>
      <polygon points="0,0 560,0 300,400 0,400" fill="#2b2b2d"/>
      <polygon points="560,0 580,0 262,400 230,400" fill="url(#silverBand)"/>
    </svg>

    <p class="back-brand">Hollin Marsh<br>Construction</p>

    <ul class="contact">
      <li>07822200444
        <svg viewBox="0 0 24 24" aria-hidden="true"><path d="M6.6 10.8a15.1 15.1 0 0 0 6.6 6.6l2.2-2.2a1 1 0 0 1 1-.25 11.4 11.4 0 0 0 3.6.57 1 1 0 0 1 1 1V20a1 1 0 0 1-1 1A17 17 0 0 1 3 4a1 1 0 0 1 1-1h3.5a1 1 0 0 1 1 1c0 1.25.2 2.45.57 3.6a1 1 0 0 1-.25 1z"/></svg>
      </li>
      <li>info@hollin-marsh
        <svg viewBox="0 0 24 24" aria-hidden="true"><path d="M2 5h20v14H2z M3.5 6.5 12 13l8.5-6.5" fill="none" stroke="#1d1d1f" stroke-width="2"/></svg>
      </li>
      <li>www.hollin-marsh.co.uk
        <svg viewBox="0 0 24 24" aria-hidden="true"><circle cx="12" cy="12" r="9" fill="none" stroke="#1d1d1f" stroke-width="2"/><path d="M3 12h18M12 3c3 3 3 15 0 18M12 3c-3 3-3 15 0 18" fill="none" stroke="#1d1d1f" stroke-width="1.6"/></svg>
      </li>
    </ul>

    <div class="person">
      <p class="person-name">Tobias Renwick</p>
      <p class="person-role">Managing Director</p>
    </div>
  </section>
</main>
</body>
</html>
```